New Website for Asia Travel Agency

Lanternpath Journeys Website

We want a redesign for our current website, www.lanternpathjourneys.example. We want you to get creative with our brand and present our company in a unique, creative and compelling way, that communicates our exotic destinations and tours, the local and authentic character of our travel consultants and the trustworthy and professional nature of our company.

Who is this company?

Lanternpath Journeys is an online tour operator specializing in providing tailor-made tours to eight destinations in Asia; Vietnam, Thailand, Laos, Cambodia, Indonesia, Myanmar, Japan and China. They were launched in mid February 2012 with headquarters in Bangkok, Thailand, and staffed by locals and expats with many years of experience in the travel industry, and who are committed to sharing their deep knowledge of, and passion for the region.

Local knowledge

Our consultants at Lanternpath Journeys are all locals – they know their destinations inside-out and draw upon invaluable first-hand experience and information when planning your tour. They have insights into local culture and tradition, they know the best places to visit, the most worthwhile experiences to have and, most importantly, they have the knowledge to create exactly the holiday you desire.

All hotels and activities featured in a Lanternpath Journeys tour are regularly inspected by our consultants to ensure the highest quality standards are met and that all information is correct and up to date.

Unforgettable Travel Experiences

Whether it's a cultural exploration or a beach holiday you're after – or a mix of both – Lanternpath Journeys has an itinerary for you – and if we don't have one, we'll tailor-make one! From the main sights to remote villages, our locally based Travel Specialists will give you unique insights into every place you visit and let you delve into known destinations from new perspectives.

Our tours offer a variety of hotel and resort options, premium stays in deluxe accommodation, heritage hotels, a five-star boutique or on the water in a junk. Tap into our experience let us create an experience unique to you – and one you will never forget.

What type of Holiday to Asia?

Our itineraries at Lanternpath Journeys are created according to different inspirations. Some travelers are interested in the History & Culture of a destination, while some like to stay active with Adventure tours. A Cross Border trip explores different countries in a single tour, while Velvet Summit tours offer the highest level of exclusivity across our destinations. There are 14 different Holiday Types to choose from, or you can mix and match ideas to create your dream vacation.

Target Market(s)

Slightly more female, aged 30-65, are creative, professional and looking for something different, something a bit unusual.

Industry/Entity Type

Boutique

Requirements
Must have
• 5 page designs:

1. Homepage
2. Tours list page for a country
3. Tour page
4. 'Be Inspired' page
5. Country page
6. Enquiry page

Our inspirations.

The following list shows websites we love and which inspire us... to give you some indication of our preferred styles, functions and layouts:

http://www.frostmeridian.example/en/ (we really like this, great personality, like the use of icons for tour types)
http://www.pebblewalks.example.uk/ (very simple design elements and layout)
http://www.sunvalecoast.example/ (great use of background image, nice simple nav bar)
http://www.roamcedarfall.example/ (we like because it has distinct personality and is well suited to the destination)
http://www.seemarlowton.example/ (clear personality through font use)
http://www.vastroving.example/ (original, unique)
http://www.wanderquill.example/long-loop-of-asia (like the map style)

Key design points:

1. You must use our existing logo (attached), but you can change the color scheme of the logo to accord with the whichever color scheme you choose for the main designs.
2. Our logo strapline is "Asia is our Lanternpath" and should be used prominently on the page to reinforce the meaning of our company name.
3. Home page and tours list pages should allow the user to see the choice of tours immediately without scrolling & Introduction copy should be minimal.
4. We and our site visitors are inspired and excited by our photography, this is an element of the site which we would like to maintain and build on, though the section page header sliders are currently too big and do not allow quick access to the section content. This is a design problem which needs a solution. Full page photographic backgrounds may be an answer?
5. Tour page should display other contextual tours, from the same country or style/type
6. We should promote press coverage in various places
7. We should display consultant profiles in various places
8. Map designs for tour page and country page, plus a modal pop out for the home page. These are complex and may have a few small photos and short descriptive text only, though this is limited by your own creativity. We will use graphics and html5/css3 so there are no creative limitations.
9. The 'Inspirations' / 'Be Inspired' page is for people who want travel and holiday ideas, who are looking for inspiration on where to go and what to do. This section needs to reflect the exotic, the unusual, the extraordinary in our destinations and tours, and we leave this to your creative genius to develop. We are also interested in how this inspirations page is related to the blog and social media content we produce daily, is there an integration here? Can we present YouTube videos, our blog posts, Facebook posts etc, on this page? This is another design challenge.
10. We would like to see designs for the tours list page which feature AJAX content filtering (for instance: http://demo.layoutbrisk.example/?acn), we would like to see how to include this type of content filtering on homepage and destination page also.
11. The 'Enquiry' call to action should be on all pages and prominent.
12. The enquiry page can reflect the same fields as the existing website enquiry page

Values to be communicated:

- Exotic: Asia is exotic, and our tours will expose clients to extraordinary sights and unusual cultural encounters.
- Authentic: Our travel consultants all live in the destinations themselves, they are local nationals and have all the insider knowledge to give clients a truly authentic experience of our destinations
- Unique: All of our tours are tailor made, there are no fixed departure dates or join-in groups. All tour itineraries can be uniquely designed for our clients, from departure dates to destinations.
- Trust: Some travelers prefer to book their holidays with local agencies they can meet in person, rather than with online companies like us who live in the destinations and who they only get to meet on Skype video or phone. We want to convey that we are trustworthy. We have attempted this through presenting a 'meet the team' page and a 'press' page and advert, as well as offering a prominent international phone number. How we you build on this and further convey this value?

```html
<!DOCTYPE html>
<html lang="en">
<head>
<meta charset="utf-8">
<title>Lanternpath Journeys — Home</title>
<link href="https://fonts.googleapis.com/css2?family=Open+Sans:wght@400;600;700&family=Source+Sans+3:wght@400;600;700&family=Raleway:wght@400;700&display=swap" rel="stylesheet">
<style>
:root{
  --sky:#1f9ad6;
  --header:#222a2c;
  --header-2:#2b3437;
  --ink:#2b2b2b;
  --muted:#555;
  --teal:#a9d3d1;
  --teal-deep:#5b9ea0;
  --ocean-top:#1a6fb0;
  --ocean-mid:#2f8cc4;
  --ocean-low:#a8cfd3;
  --card:#ffffff;
  --line:#e3e3e3;
  --footer:#242a2c;
  --footer-base:#1c2123;
  --footer-text:#d8dede;
  --red:#d62027;
}
*{box-sizing:border-box;margin:0;padding:0}
html,body{width:907px;height:1200px;overflow:hidden}
body{position:relative;font-family:"Source Sans 3",sans-serif;color:var(--ink);background:var(--footer)}
.abs{position:absolute}

.top-strip{left:0;top:0;width:907px;height:8px;background:var(--sky)}
.site-header{left:0;top:8px;width:907px;height:64px;background:linear-gradient(var(--header-2),var(--header))}
.brand{left:88px;top:22px;display:flex;align-items:center;gap:8px}
.brand-mark{width:26px;height:26px;background:#cfe3e4;border-radius:4px}
.brand-text{color:#fff;font-family:"Open Sans",sans-serif;font-weight:600;font-size:15px;line-height:1}
.brand-tag{color:#fff;font-family:"Open Sans",sans-serif;font-weight:600;font-size:7px;left:150px;top:49px}
.main-nav{left:319px;top:29px;display:flex;font-family:"Open Sans",sans-serif;font-size:11.5px;color:#fff}
.main-nav a{color:#fff;text-decoration:none;height:22px;line-height:22px;display:flex;align-items:center;gap:3px}
.main-nav .active{background:#3e4a4d;padding:0 10px;margin-right:16px}
.main-nav .item{margin-right:28px}
.main-nav svg{width:7px;height:5px}

.ocean{left:0;top:72px;width:907px;height:944px;background:linear-gradient(180deg,var(--ocean-top) 0%,var(--ocean-mid) 30%,#4a9fc7 48%,#8cc2cd 62%,var(--ocean-low) 100%)}

.headline{left:77px;top:186px;width:478px;height:46px;background:var(--teal);clip-path:polygon(0 0,100% 0,91% 100%,0 100%)}
.headline h1{font-family:"Open Sans",sans-serif;font-weight:700;font-size:27px;color:#1f2a2c;padding:6px 0 0 4px;letter-spacing:.2px;white-space:nowrap}
.subline{left:77px;top:232px;width:368px;height:37px;background:#222a2c}
.subline p{font-family:"Raleway",sans-serif;font-size:18.5px;color:#fff;padding:6px 0 0 5px;white-space:nowrap}

.search{left:590px;top:134px;width:236px;height:198px;background:rgba(34,42,44,.95);border-radius:7px}
.search .tab-on{left:8px;top:8px;font-family:"Open Sans",sans-serif;font-size:13.5px;color:#fff}
.search .tab-off{left:118px;top:0;width:118px;height:28px;background:#eef3f3;border-radius:0 7px 0 0;clip-path:polygon(6% 0,100% 0,100% 100%,0 100%);font-family:"Open Sans",sans-serif;font-size:13.5px;color:#222;padding:5px 0 0 14px}
.search b{font-weight:600}
.field-label{font-family:Arial,sans-serif;font-size:8px;color:#fff;text-align:right;width:60px;line-height:9.5px}
.select{width:161px;height:24px;background:#fff;border-radius:3px;font-family:Arial,sans-serif;font-size:9.5px;color:#555;padding:6px 0 0 7px}
.select i{position:absolute;right:6px;top:6px;width:12px;height:12px;background:#222}
.select i:after{content:"";position:absolute;left:3px;top:4px;border:3px solid transparent;border-top:4px solid #fff}
.btn-light{height:23px;background:linear-gradient(#f4f4f4,#cfcfcf);border-radius:2px;font-family:Arial,sans-serif;font-size:10.5px;color:#222;text-align:center;line-height:23px}
.btn-teal{background:linear-gradient(#d7ecea,var(--teal))}

.card{left:77px;top:356px;width:753px;height:692px;background:var(--card);border-radius:3px}
.quote{left:89px;top:370px;width:730px;font-size:14.4px;line-height:21.2px;color:#333}
.quote .mark{font-family:Georgia,serif;font-size:22px;color:#333;line-height:0}
.quote .hl{background:#bfe0de}
.divider{left:89px;top:483px;width:726px;border-top:1px dotted #aaa}

.panel{border:1px solid var(--line);box-shadow:0 0 3px rgba(0,0,0,.08);background:#fff}
.tab{font-family:"Source Sans 3",sans-serif;font-weight:600;font-size:14px;letter-spacing:.3px;color:#222;background:#fff;border:1px solid var(--line);border-bottom:none;border-radius:4px 4px 0 0;text-align:center;white-space:nowrap}
.photo{border:2px solid #e5e5e5}
.arrow{width:20px;height:28px}

.why-text{left:610px;top:552px;width:185px;font-family:Arial,sans-serif;font-size:10.4px;line-height:16.6px;color:#333}
.readmore{left:700px;top:702px;width:76px;height:20px;background:#ebebeb;border-radius:10px 10px 0 0;font-family:Arial,sans-serif;font-weight:700;font-size:10px;color:#333;text-align:center;line-height:20px}

.tour{left:98px;top:752px;width:706px;height:240px;border:1px solid var(--line);border-radius:4px;box-shadow:0 0 3px rgba(0,0,0,.08)}
.tour-head{left:98px;top:752px;width:706px;height:33px;background:linear-gradient(#3b4446,#1f2628);border-radius:4px 4px 0 0}
.tour-head h2{font-family:"Source Sans 3",sans-serif;font-weight:600;font-size:13.5px;color:#fff;letter-spacing:.4px;padding:7px 0 0 18px}
.label{font-family:"Source Sans 3",sans-serif;font-size:11px;letter-spacing:.6px;color:#333}
.value{font-family:"Source Sans 3",sans-serif;font-size:11px;letter-spacing:.4px;color:#222}
.small{font-family:Arial,sans-serif;font-size:8px;color:#3a7c8a}
.body-sm{font-family:Arial,sans-serif;font-size:9.8px;line-height:13.8px;color:#333}
.send{left:692px;top:959px;width:98px;height:23px;background:#243033;border-radius:3px;color:#fff;font-family:Arial,sans-serif;font-weight:700;font-size:9.5px;text-align:center;line-height:23px}
.view{left:626px;top:966px;font-family:Arial,sans-serif;font-size:8.5px;color:#333}
.more-bar{left:98px;top:1008px;width:706px;height:28px;background:linear-gradient(#d6ebea,var(--teal));border-radius:4px;font-family:Arial,sans-serif;font-weight:700;font-size:10px;color:#333;text-align:center;line-height:28px}

.foot-col{font-family:"Source Sans 3",sans-serif;font-size:10.5px;color:var(--footer-text);list-style:none;line-height:16.8px}
.foot-col li:before{content:"»";color:#9aa6a6;margin-right:6px;font-size:9px}
.vline{width:1px;top:1062px;height:112px;background:#394244}
.news-title{left:576px;top:1066px;font-family:"Source Sans 3",sans-serif;font-weight:600;font-size:13.5px;color:#9cc7c6}
.news-text{left:576px;top:1093px;width:232px;font-family:"Source Sans 3",sans-serif;font-weight:600;font-size:8.8px;line-height:13.6px;color:#fff}
.news-input{left:576px;top:1128px;width:191px;height:29px;background:#5f6667;border-radius:3px 0 0 3px}
.news-btn{left:766px;top:1128px;width:35px;height:29px;background:var(--teal-deep);border-radius:0 3px 3px 0}
.base{left:0;top:1178px;width:907px;height:22px;background:var(--footer-base);font-family:"Source Sans 3",sans-serif;font-size:8px;color:#7d8788;text-align:center;line-height:18px}
</style>
</head>
<body>
<div class="abs ocean" role="img" aria-label="Underwater coral reef scene with tropical fish, fading to pale sea"></div>
<div class="abs top-strip"></div>
<header class="abs site-header"></header>
<div class="abs brand"><span class="brand-mark"></span><span class="brand-text">Lanternpath Journeys</span></div>
<div class="abs brand-tag">Asia is our Lanternpath.</div>
<nav class="abs main-nav">
  <a class="active">Home</a>
  <a class="item">Destinations <svg viewBox="0 0 7 5"><path d="M.5.5 3.5 4 6.5.5" stroke="#fff" fill="none"/></svg></a>
  <a class="item">Tours <svg viewBox="0 0 7 5"><path d="M.5.5 3.5 4 6.5.5" stroke="#fff" fill="none"/></svg></a>
  <a class="item">Holiday Types <svg viewBox="0 0 7 5"><path d="M.5.5 3.5 4 6.5.5" stroke="#fff" fill="none"/></svg></a>
  <a class="item">Best Value</a>
  <a class="item">About Us</a>
  <a>Blog</a>
</nav>

<div class="abs headline"><h1>ASIA IS OUR LANTERNPATH</h1></div>
<div class="abs subline"><p>No one knows a destination better than</p></div>

<section class="abs search">
  <div class="abs tab-on"><b>Tours</b> Search</div>
  <div class="abs tab-off"><b>Hotel</b> Search</div>
  <div class="abs field-label" style="left:-2px;top:47px">SELECT<br>A COUNTRY:</div>
  <div class="abs select" style="left:66px;top:45px">All Countries<i></i></div>
  <div class="abs field-label" style="left:-2px;top:88px">SELECT<br>A CITY:</div>
  <div class="abs select" style="left:66px;top:86px">All Countries<i></i></div>
  <div class="abs field-label" style="left:1px;top:131px">DURATION:</div>
  <div class="abs select" style="left:66px;top:123px">All Countries<i></i></div>
  <div class="abs btn-light" style="left:24px;top:161px;width:62px">SEARCH</div>
  <div class="abs btn-light btn-teal" style="left:107px;top:161px;width:119px">ADVANCED SEARCH</div>
</section>

<div class="abs card"></div>
<p class="abs quote"><span class="mark">“</span> No one knows a <span class="hl">Destination better than someone who lives, works and plays there.</span> That's the foundation of Lanternpath Journeys. Our travel specialists reside in Asia. They live Asia, they breathe Asia. And they're in-trigued explorers as much as they are citizens of Bangkok, or Bali, or Luang Prabang. The result is a travel company tailor-made for the person with a taste for veering.<span class="mark">”</span></p>
<div class="abs divider"></div>

<div class="abs panel" style="left:99px;top:537px;width:310px;height:185px"></div>
<div class="abs tab" style="left:99px;top:506px;width:161px;height:33px;line-height:32px">Hot Destinations</div>
<div class="abs" style="left:262px;top:506px;width:140px;line-height:32px;text-align:center;font-weight:600;font-size:14px;letter-spacing:.3px;color:#444">New Creations</div>
<div class="abs photo" role="img" aria-label="Turquoise lake with waterfall and green cliffs" style="left:142px;top:565px;width:221px;height:137px;background:linear-gradient(180deg,#6fb1e0 0%,#bfe0f2 25%,#4f9a4a 45%,#2f7a46 65%,#1fa3c4 80%,#0c6f9c 100%)"></div>
<svg class="abs arrow" style="left:113px;top:623px" viewBox="0 0 20 28"><path d="M15 2 4 14l11 12" stroke="#111" stroke-width="5" fill="none"/></svg>
<svg class="abs arrow" style="left:374px;top:623px" viewBox="0 0 20 28"><path d="M5 2l11 12L5 26" stroke="#111" stroke-width="5" fill="none"/></svg>

<div class="abs panel" style="left:433px;top:539px;width:371px;height:183px"></div>
<div class="abs tab" style="left:433px;top:507px;width:196px;height:34px;line-height:33px">Why Lanternpath Journeys</div>
<div class="abs photo" role="img" aria-label="Family paddling a canoe in life jackets" style="left:454px;top:554px;width:143px;height:151px;background:linear-gradient(160deg,#6c747a,#a6adb1 50%,#56606a)"></div>
<p class="abs why-text"><b>What makes a travel company expert</b> on the destinations it builds trips to? Some might say spending a few weeks a year in those destina-tions. At Lanternpath Journeys, we're on the ground year-round, with our fin-gers always on the pulse of what's new and what's happening.</p>
<div class="abs readmore">Read More..</div>

<div class="abs tour"></div>
<div class="abs tour-head"><h2>A TALE OF TWO CITIES: MANDALAY TO BAGAN</h2></div>
<div class="abs photo" role="img" aria-label="Colonial-style hotel building under a blue sky with palms" style="left:114px;top:809px;width:204px;height:137px;background:linear-gradient(180deg,#2c6fc4 0%,#7fb1e6 35%,#e1d3aa 55%,#c9b385 70%,#4a7a3a 85%,#8a8a80 100%)"></div>
<div class="abs label" style="left:341px;top:811px">PROMOTION PRICE</div>
<div class="abs value" style="left:486px;top:811px">$424 (10% Off)</div>
<div class="abs small" style="left:487px;top:826px">Price Per Person</div>
<div class="abs label" style="left:341px;top:846px">DURATION</div>
<div class="abs value" style="left:486px;top:846px">4 DAYS / 3 NIGHTS</div>
<div class="abs label" style="left:341px;top:876px">FAST FACTS</div>
<p class="abs body-sm" style="left:485px;top:874px;width:300px">See the hidden treasures of Sambor Prey Kuk. The temples are 100 years older than Angkor!</p>
<p class="abs body-sm" style="left:340px;top:911px;width:450px">The perfect tailor-made temple trip for all the family, this Lanternpath Journeys tour allows you to expe-rience the best of the majestic region of Cambodia's Angkor region.</p>
<svg class="abs" style="left:656px;top:792px" width="78" height="78" viewBox="0 0 78 78" role="img" aria-label="Best value badge"><circle cx="39" cy="39" r="37" fill="var(--red)"/><circle cx="39" cy="39" r="30" fill="none" stroke="#fff" stroke-width="2"/></svg>
<div class="abs view">VIEW TOUR <b>+</b></div>
<div class="abs send">SEND AN INQUIRY</div>
<div class="abs more-bar">More <svg width="8" height="6" viewBox="0 0 8 6"><path d="M1 1l3 2 3-2M1 3.5l3 2 3-2" stroke="#333" fill="none"/></svg></div>

<ul class="abs foot-col" style="left:108px;top:1061px"><li>Home</li><li>Destinations</li><li>Tours</li><li>Holiday Types</li><li>Best Value</li><li>About Us</li></ul>
<div class="abs vline" style="left:236px"></div>
<ul class="abs foot-col" style="left:266px;top:1064px"><li>Thailand</li><li>Indonesia</li><li>Laos</li><li>Cambodia</li><li>Japan</li><li>Myanmar</li></ul>
<div class="abs vline" style="left:371px"></div>
<ul class="abs foot-col" style="left:402px;top:1064px"><li>Why Book With Us</li><li>About Us</li><li>Meet The Team</li><li>Careers</li><li>In The Press</li><li>Affiliate Program</li></ul>
<div class="abs vline" style="left:538px"></div>
<div class="abs news-title">Join Our Newsletter</div>
<p class="abs news-text">Stay up to date with all our latest tips to improve your websites performance with our newsletter.</p>
<div class="abs news-input"></div>
<div class="abs news-btn"><svg width="35" height="29" viewBox="0 0 35 29"><circle cx="16" cy="14" r="7" fill="none" stroke="#fff" stroke-width="1.6"/><path d="M9 14h14M16 7v14" stroke="#fff" stroke-width="1"/><path d="M21 19l6 5" stroke="#fff" stroke-width="2.4"/></svg></div>
<div class="abs base">© 2013 Lanternpath Journeys. All Rights Reserved</div>
</body>
</html>
```